BRIX Rentals ( Website Graphic design ) small property management new business ( real estate )

I need a website designed for a new small Property Management ( no sales ) company I'm starting up soon. I have a design in mind that I like and would like to keep it quite similar to this if possible using my logo and colour scheme and slightly ALTER the layout. and maybe a little more interactive with some motion and images etc
Please see the link to show the simplicity I'm after. I want to be bold ad very clear and concise. I love the simplicity of this design but not necessarily the pages with just text on them. I would want them to be a bit more interesting with some pictures and photos. http://www.lindavostrel.com.au/

The branding on the site should be bold and very sharp.

My target market is the mid to high end of the rental market in Darwin Australia and should reflect "good quality, outstanding service and attention to detail, energetic, integrity, "

I will only require a few pages to start with, Home / Company Profile / Management Services / Owners information / Tenant information / Properties and About Darwin. I will be able to provide text for each of the pages but would be no more than 4-6 paragraphs apart from the management services page which would detail a number of the services we would offer. The properties page will just be a link to homelistz,com.au to show my listings and then a couple more links to owner and tenant portals, chatterbox page etc. It must also be responsive to mobile devices.

I would also like to include a chatterbox page design and build.

regards
Marta Penhale

Target Market(s)

property owners, investors, Darwin Australia, renters, ages 30 - 60, tenants

Industry/Entity Type

Property Management

Font styles to use
Other font styles liked:
• i like helvetica, but not essential

Requirements
Must have
• Clean and crisp pages, not busy , responsive to devices
• links to portals and chatterbox, any ability to add other links at a later date.
Nice to have
• music - must be upbeat but not over the top
Should not have
• be too busy on each page

```html
<!DOCTYPE html>
<html lang="en">
<head>
<meta charset="utf-8">
<title>Tallow Conveyancing</title>
<link rel="stylesheet" href="https://fonts.googleapis.com/css2?family=Open+Sans:wght@400;600&display=swap">
<style>
  :root {
    --teal: #008b8f;
    --panel: #4f4d4e;
    --panel-line: #5f5d5e;
    --white: #ffffff;
    --nav-text: #ebebeb;
    --body-text: #4a4a4a;
    --footer-text: #c8c8c8;
    --social-text: #b8b8b8;
    --bullet: #cfcfcf;
    --photo-sky: #3d4f86;
    --photo-house: #8a6a4c;
    --photo-pool: #3fb3b6;
  }
  * { box-sizing: border-box; margin: 0; padding: 0; }
  html, body { width: 1200px; height: 1020px; overflow: hidden; }
  body {
    position: relative;
    background: var(--teal);
    font-family: "Open Sans", Helvetica, Arial, sans-serif;
  }

  .brand {
    position: absolute; left: 400px; top: 78px; width: 380px;
    text-align: center;
    color: var(--white); font-size: 30px; font-weight: 400; line-height: 1.2;
  }

  .main-panel {
    position: absolute; left: 70px; top: 286px; width: 1050px; height: 463px;
    background: var(--panel); border-radius: 12px;
  }
  .site-nav { position: absolute; left: 20px; top: 36px; width: 250px; list-style: none; }
  .site-nav li {
    height: 45.5px; display: flex; align-items: center; gap: 10px;
    border-bottom: 1px solid var(--panel-line);
    color: var(--nav-text); font-size: 14.5px; padding-left: 3px;
  }
  .nav-bullet { width: 12px; height: 12px; flex: none; }

  .services { position: absolute; left: 784px; top: 50px; width: 248px; }
  .services-title {
    color: var(--teal); font-size: 24px; font-weight: 400;
    padding-bottom: 14px; border-bottom: 1px solid var(--panel-line);
  }
  .services-list { list-style: none; margin-top: 10px; }
  .services-list li {
    height: 34px; display: flex; align-items: center; gap: 10px;
    color: var(--nav-text); font-size: 14.5px;
  }
  .tri { width: 6px; height: 7px; flex: none; }

  .feature-card {
    position: absolute; left: 359px; top: 246px; width: 472px; height: 554px;
    background: var(--white); border-radius: 12px;
  }
  .feature-photo {
    position: absolute; left: 14px; top: 18px; width: 444px; height: 343px;
    background: linear-gradient(180deg, var(--photo-sky) 0%, var(--photo-house) 45%, var(--photo-pool) 75%, #2b8f96 100%);
  }
  .feature-text {
    position: absolute; left: 14px; top: 386px; width: 440px;
    color: var(--body-text); font-size: 14px; line-height: 25px;
  }
  .feature-text p + p { margin-top: 24px; }

  .site-footer {
    position: absolute; left: 70px; top: 976px; width: 1050px; height: 44px;
    background: var(--panel); border-radius: 10px 10px 0 0;
    display: flex; align-items: center; justify-content: space-between;
    padding: 0 24px;
  }
  .copyright { color: var(--footer-text); font-size: 13.5px; }
  .social { display: flex; gap: 14px; list-style: none; }
  .social li { color: var(--social-text); font-size: 13px; font-weight: 600; }
</style>
</head>
<body>
  <header class="brand">Tallow Advisory</header>

  <section class="main-panel">
    <ul class="site-nav">
      <li><svg class="nav-bullet" viewBox="0 0 12 12"><circle cx="6" cy="6" r="5" fill="none" stroke="#cfcfcf" stroke-width="1.2"/><circle cx="6" cy="6" r="2" fill="#cfcfcf"/></svg>&nbsp;Home</li>
      <li><svg class="nav-bullet" viewBox="0 0 12 12"><circle cx="6" cy="6" r="5" fill="none" stroke="#cfcfcf" stroke-width="1.2"/><circle cx="6" cy="6" r="2" fill="#cfcfcf"/></svg>Company Profile</li>
      <li><svg class="nav-bullet" viewBox="0 0 12 12"><circle cx="6" cy="6" r="5" fill="none" stroke="#cfcfcf" stroke-width="1.2"/><circle cx="6" cy="6" r="2" fill="#cfcfcf"/></svg>Management Services</li>
      <li><svg class="nav-bullet" viewBox="0 0 12 12"><circle cx="6" cy="6" r="5" fill="none" stroke="#cfcfcf" stroke-width="1.2"/><circle cx="6" cy="6" r="2" fill="#cfcfcf"/></svg>Owners information</li>
      <li><svg class="nav-bullet" viewBox="0 0 12 12"><circle cx="6" cy="6" r="5" fill="none" stroke="#cfcfcf" stroke-width="1.2"/><circle cx="6" cy="6" r="2" fill="#cfcfcf"/></svg>Tenant information</li>
      <li><svg class="nav-bullet" viewBox="0 0 12 12"><circle cx="6" cy="6" r="5" fill="none" stroke="#cfcfcf" stroke-width="1.2"/><circle cx="6" cy="6" r="2" fill="#cfcfcf"/></svg>Properties &amp; About Darwin.</li>
    </ul>

    <aside class="services">
      <h2 class="services-title">Our services</h2>
      <ul class="services-list">
        <li><svg class="tri" viewBox="0 0 6 7"><path d="M0 0L6 3.5L0 7Z" fill="#bdbdbd"/></svg>Residential property settlements</li>
        <li><svg class="tri" viewBox="0 0 6 7"><path d="M0 0L6 3.5L0 7Z" fill="#bdbdbd"/></svg>Vacant land property settlements</li>
        <li><svg class="tri" viewBox="0 0 6 7"><path d="M0 0L6 3.5L0 7Z" fill="#bdbdbd"/></svg>Commercial property settlements</li>
        <li><svg class="tri" viewBox="0 0 6 7"><path d="M0 0L6 3.5L0 7Z" fill="#bdbdbd"/></svg>Rural property settlements</li>
        <li><svg class="tri" viewBox="0 0 6 7"><path d="M0 0L6 3.5L0 7Z" fill="#bdbdbd"/></svg>Off-the-Plan developments</li>
        <li><svg class="tri" viewBox="0 0 6 7"><path d="M0 0L6 3.5L0 7Z" fill="#bdbdbd"/></svg>Private sales</li>
      </ul>
    </aside>
  </section>

  <article class="feature-card">
    <div class="feature-photo" role="img" aria-label="Tropical villa with lit pavilion roof beside a turquoise pool at dusk"></div>
    <div class="feature-text">
      <p>Tallow Conveyancing is a specialised real estate settlement agency committed to delivering an exclusive settlement service.</p>
      <p>The agency was founded in 2008 by licensee Linda Vostrel who achieved a substantial part of her 14 years previous conveyancing experience at a range of Perth legal firms.</p>
    </div>
  </article>

  <footer class="site-footer">
    <p class="copyright">Copyright © 2015 tallowadvisory.com All Rights Reserved.</p>
    <ul class="social">
      <li>chirper</li>
      <li>chatterbox</li>
      <li>loopward</li>
    </ul>
  </footer>
</body>
</html>
```